Business Card Design Project

After recently finishing a design project for the company logo using artfoundry, it's now time for a business card. Attached to this is the logo.

The requirements for the business card are pretty straightforward:

- A clean, uncomplicated look
- Consistent usage of fonts
- Designs for both single sided and double sided cards
- A modern layout with preferably space to refer to social media accounts and/or downloadable vcards through a qr code
- consistent application of the company colour scheme: red/white. Hex codes for exact colour can be provided

Thanks!

```html
<!DOCTYPE html>
<html lang="en">
<head>
<meta charset="utf-8">
<title>Kiln Row Recruiting — Business Cards</title>
<link href="https://fonts.googleapis.com/css2?family=Arimo:wght@400;700&display=swap" rel="stylesheet">
<style>
  :root {
    --brand-red: #e31e26;
    --ink: #1a1a1a;
    --card-white: #ffffff;
    --watermark-grey: #e6e6e6;
    --page-bg: #ecebe8;
    --card-shadow: rgba(0, 0, 0, 0.18);
  }
  * { box-sizing: border-box; margin: 0; padding: 0; }
  html, body {
    width: 1200px;
    height: 900px;
    overflow: hidden;
    background: var(--page-bg);
    font-family: "Arimo", Arial, sans-serif;
  }
  .sheet {
    position: relative;
    width: 1200px;
    height: 900px;
  }
  .card {
    position: absolute;
    left: 320px;
    width: 560px;
    height: 320px;
    background: var(--card-white);
    box-shadow: 0 3px 12px var(--card-shadow);
    overflow: hidden;
  }
  .card--back { top: 100px; }
  .card--front { top: 480px; }

  /* wordmark lockup */
  .wordmark {
    display: flex;
    align-items: center;
    gap: 10px;
    color: var(--brand-red);
    font-weight: 700;
    white-space: nowrap;
  }
  .wordmark__square {
    width: 20px;
    height: 20px;
    background: var(--brand-red);
    flex: none;
  }
  .wordmark__name { font-size: 22px; letter-spacing: 0.3px; }

  /* back face */
  .card--back .wordmark {
    position: absolute;
    left: 56px;
    top: 168px;
  }
  .qr-slot {
    position: absolute;
    left: 330px;
    top: 60px;
    width: 170px;
    height: 150px;
    background: var(--brand-red);
    display: flex;
    align-items: center;
    justify-content: center;
  }
  .qr-slot__label {
    font-size: 10px;
    font-weight: 700;
    color: var(--ink);
  }

  /* front face */
  .top-band {
    position: absolute;
    left: 0; top: 0;
    width: 100%;
    height: 20px;
    background: var(--brand-red);
  }
  .watermark {
    position: absolute;
    left: 18px;
    top: 34px;
    font-size: 118px;
    font-weight: 700;
    color: var(--watermark-grey);
    letter-spacing: -2px;
    white-space: nowrap;
    line-height: 1;
  }
  .logo-plate {
    position: absolute;
    left: 60px;
    top: 150px;
    width: 250px;
    height: 74px;
    background: var(--card-white);
    box-shadow: 0 2px 6px rgba(0, 0, 0, 0.2);
    display: flex;
    align-items: center;
    padding-left: 18px;
  }
  .logo-plate .wordmark__name { font-size: 20px; }
  .contact {
    position: absolute;
    left: 350px;
    top: 150px;
    display: grid;
    grid-template-columns: auto auto;
    column-gap: 14px;
    row-gap: 3px;
    font-size: 11px;
    line-height: 1.3;
  }
  .contact__label { font-weight: 700; color: var(--ink); }
  .contact__value { color: var(--brand-red); font-weight: 700; }
</style>
</head>
<body>
<main class="sheet">

  <section class="card card--back" aria-label="Card back">
    <div class="wordmark">
      <span class="wordmark__square"></span>
      <span class="wordmark__name">Kiln Row Recruiting</span>
    </div>
    <div class="qr-slot">
      <span class="qr-slot__label">Your QR code here</span>
    </div>
  </section>

  <section class="card card--front" aria-label="Card front">
    <div class="top-band"></div>
    <div class="watermark" aria-hidden="true">Kiln Row</div>
    <div class="logo-plate">
      <div class="wordmark">
        <span class="wordmark__square"></span>
        <span class="wordmark__name">Kiln Row Recruiting</span>
      </div>
    </div>
    <dl class="contact">
      <dt class="contact__label">Name:</dt>
      <dd class="contact__value">Jonathan Doe</dd>
      <dt class="contact__label">Phone:</dt>
      <dd class="contact__value">(000) 123 - 4567</dd>
      <dt class="contact__label">Email:</dt>
      <dd class="contact__value">jdoe@kilnrow.example</dd>
    </dl>
  </section>

</main>
</body>
</html>
```